かなり豪華な(市販価格1,890円)フルカラーのカタログを自社製作しており、
それをホームページ上で無料でプレゼントしています。
現在はこのようなページになっています。
http://www.tamasou-niwa.com/contact/
いろいろな資料が同時に請求できるようになっていますが、
今回依頼したいのは、施工事例カタログ専用のランディングページです。

イメージは、森市のヒット商品の販売ページみたいな感じです。
(安っぽいデザインのページが多いので、もっと高級感を出したいですが)
こちらのサイトでいろいろ作例が載っていました。
http://www.hanaso-works.jp/theme18.html

こんな感じも好きです。
http://bemoto.co.jp/recruit/legend-designer/

1ページの構成にしたいですが、
あまりタテに長く作りたくありません。
モニター2画面分くらいで収めたいです。

カタログの特徴はこちらです。
■フルカラー・300ページ。
■エクステリアの施工例に特化したカタログは希少。
■価格が載っているので、自宅を工事する場合の金額のイメージが付けやすい。
■定価1890円でポルカスで販売中のものが無料でもらえる。

http://www.tamasou-niwa.com/
1ページ
グリーン・ベージュ・ブラウン・ブラック
• 高解像度JPG (.jpg)
• イラストレーター形式 (.ai)
古いカタログの画像ですが、製作用の参考に添付しておきます。
http://okuribin.jp/download/1f0e2d3c4b5a69788796a5b4c3d2e1f0a9b8c7d6

画像等の素材もアップしました。
http://okuribin.jp/download/2e1f3a4b5c6d7e8f9a0b1c2d3e4f5a6b7c8d9e0f
http://okuribin.jp/download/3d2c1b0a9f8e7d6c5b4a3f2e1d0c9b8a7f6e5d4c

ご提案の際はダミーのカタログ画像などで行っていただき、
当選の方には実際のカタログをご送付し、最終的に仕上げていただきます。
よろしくお願いします。
訴求のポイントについてご質問いただきましたので、
一つ付け加えたいと思います。

「制作費が非常に高いため、在庫が無くなり次第終了です」
というような言葉をつかっていただけますか?
※言い方はこの通りでなくてもOKです。

今回のページはリスティング広告用のランディングページになりますので、資料請求(=カタログの無料プレゼントへの申し込み)をしてもらうことが最大の目的です。そのためには、無料であること、豪華なこと、内容が濃いことなどを訴求していただければと思います。

よろしくお願いします。
よろしくお願いします。
>1ページの構成にしたいですが、
>あまりタテに長く作りたくありません。
>モニター2画面分くらいで収めたいです。

依頼内容にこのように記載しましたが、
これは無視していただいてかまいません。
※どれだけタテに長くなってもOKです。
ご提案ありがとうございます。
一つ注意点があります。
サイト訪問者に動作をしてもらうようなページはNGでお願いします。
(クリックしてページをめくるなど)
動作に凝らなくい方がいいですし、ビジュアルも然りです。
単純にこの一覧のようなページでかまいません。
http://www.peji-narabe.jp/
よろしくお願いします。
素材のアップロード期限が過ぎてしまったため、
こちらに再アップしました。

http://okuribin.jp/download/4c5d6e7f8a9b0c1d2e3f4a5b6c7d8e9f0a1b2c3d

http://okuribin.jp/download/5b6a7f8e9d0c1b2a3f4e5d6c7b8a9f0e1d2c3b4a

http://okuribin.jp/download/6a7b8c9d0e1f2a3b4c5d6e7f8a9b0c1d2e3f4a5b

よろしくお願いします。

デザインの第一印象がとてもよく、コンテンツも見やすくまとまっており、高いコンバージョンが期待できる作品だと思いました。

魅力的なご提案をありがとうございました。
こういったデザインコンペは今後も複数依頼予定ですので、次回もよろしくお願いします。

```html
<!DOCTYPE html>
<html lang="ja">
<head>
<meta charset="utf-8">
<title>玉草工房 エクステリア施工例カタログ 無料プレゼント</title>
<link href="https://fonts.googleapis.com/css2?family=Noto+Sans+JP:wght@400;700;900&family=Noto+Serif+JP:wght@500;700;900&display=swap" rel="stylesheet">
<style>
:root{
  --green:#7fb23a;
  --green-dark:#5c8a22;
  --green-pale:#eef5df;
  --beige:#f4efe3;
  --brown:#5a3d25;
  --brown-light:#8a6a45;
  --orange:#e98a17;
  --red:#c8322a;
  --ink:#2b2118;
  --white:#ffffff;
}
*{box-sizing:border-box;margin:0;padding:0}
html,body{width:1200px;height:3696px;overflow:hidden}
body{background:var(--white);color:var(--ink);font-family:"Noto Sans JP",sans-serif;position:relative}
.serif{font-family:"Noto Serif JP",serif}
section,header,footer{position:absolute;left:0;width:1200px}
.abs{position:absolute}
.ph{position:absolute}

/* header */
.site-header{top:0;height:150px;background:var(--white)}
.brand{left:24px;top:34px;display:flex;align-items:center;gap:10px}
.brand .mark{width:22px;height:22px;background:var(--brown);flex:none}
.brand span{color:var(--brown);font-weight:700;font-size:28px;letter-spacing:2px}
.site-header .tagline{left:220px;top:20px;font-size:13px;color:#555;line-height:1.6;width:560px}
.contact-btn{right:24px;top:14px;width:350px;height:70px;background:var(--red);border-radius:8px;color:var(--white);display:flex;align-items:center;gap:12px;padding:0 16px;font-size:17px;font-weight:700;line-height:1.35}
.contact-btn .icon{width:34px;height:34px;border-radius:50%;background:var(--white);display:flex;align-items:center;justify-content:center;flex:none}

/* hero */
.hero{top:150px;height:860px;background:linear-gradient(#f3f3f1,#e4e4e0)}
.hero-headline{left:330px;top:170px;width:560px;text-align:center;font-weight:900}
.hero-headline .l1{font-size:96px;color:var(--ink);line-height:1.1}
.hero-headline .l2{font-size:88px;color:var(--red);line-height:1.2;margin-left:120px}
.hero-copy{left:40px;top:455px;width:580px;font-size:19px;line-height:1.7;color:#333}
.hero-copy .em{color:var(--red);font-size:26px;font-weight:700}
.free-badge{left:870px;top:250px;width:300px;height:300px;border-radius:50%;background:var(--white);border:8px solid var(--green);text-align:center;padding-top:42px;color:var(--green-dark);font-weight:900}
.free-badge .now{font-size:36px;line-height:1.2}
.free-badge .free{font-size:60px;line-height:1.15}
.free-badge .gift{font-size:24px;background:var(--green);color:var(--white);display:inline-block;padding:2px 12px;margin-top:4px}
.safe-badge{left:30px;top:640px;width:230px;height:170px;background:var(--green);border-radius:80px 10px 80px 10px;color:var(--white);font-weight:900;font-size:32px;line-height:1.3;display:flex;align-items:center;justify-content:center;text-align:center}
.service-banner{left:290px;top:690px;width:860px;height:80px;background:var(--white);border-top:4px dotted var(--green);border-bottom:4px dotted var(--green);font-size:46px;font-weight:900;text-align:center;line-height:72px;color:var(--ink)}
.flow{left:30px;top:840px;width:1140px;height:58px;display:flex;gap:6px}
.flow li{list-style:none;flex:1;background:var(--brown-light);color:var(--white);font-weight:700;font-size:20px;display:flex;align-items:center;justify-content:center;clip-path:polygon(0 0,92% 0,100% 50%,92% 100%,0 100%,8% 50%)}
.flow li:first-child{clip-path:polygon(0 0,92% 0,100% 50%,92% 100%,0 100%)}

/* catalog */
.catalog{top:1090px;height:400px;background:var(--white)}
.catalog-cover{left:30px;top:40px;width:290px;height:330px;background:linear-gradient(#3a3026,#1f1914)}
.catalog-cover .ribbon{position:absolute;left:0;top:0;width:100%;height:44px;background:var(--red);color:var(--white);font-weight:700;font-size:18px;line-height:44px;text-align:center}
.catalog h2{left:360px;top:60px;font-size:40px;color:var(--red);font-weight:900}
.catalog .body{left:360px;top:130px;width:590px;font-size:22px;line-height:1.7;font-weight:700}
.catalog .note{left:360px;top:230px;width:600px;font-size:16px;line-height:1.7;color:#555}
.cta-btn{left:360px;top:300px;width:440px;height:64px;background:var(--orange);color:var(--white);font-size:26px;font-weight:900;border-radius:6px;display:flex;align-items:center;justify-content:center;gap:14px}
.plan-bubble{left:960px;top:40px;width:230px;height:230px;border-radius:50%;border:3px dashed var(--red);color:var(--red);font-weight:900;font-size:20px;line-height:1.5;display:flex;align-items:center;justify-content:center;text-align:center;padding:10px;white-space:nowrap}

/* premium */
.premium{top:1480px;height:440px}
.premium-panel{left:20px;top:20px;width:420px;height:400px;background:var(--green);color:var(--white);padding:24px 26px}
.premium-panel .kicker{font-size:22px}
.premium-panel .big{font-size:70px;font-weight:900;line-height:1.1;font-family:"Noto Serif JP",serif}
.premium-panel .sub{font-size:24px;font-weight:700;margin:4px 0 14px}
.premium-panel p{font-size:15px;line-height:1.8}
.premium-photos{left:460px;top:20px;width:720px;height:400px}

/* strengths */
.strengths{top:1950px;height:780px;text-align:center}
.strengths h2{left:0;top:20px;width:1200px;font-size:44px;line-height:1.45;font-weight:900}
.pillars{left:200px;top:180px;width:800px;display:flex;justify-content:space-between}
.pillar{width:240px;height:240px;border-radius:50%;background:var(--beige);display:flex;flex-direction:column;align-items:center;justify-content:center}
.pillar .label{font-size:20px;color:var(--brown);margin-bottom:12px}
.pillar .word{width:100%;background:var(--green);color:var(--white);font-weight:900;font-size:28px;padding:8px 0;line-height:1.2}
.no-list{left:250px;top:475px;width:700px;display:flex;justify-content:space-between}
.no-item{width:200px;height:86px;border-radius:50%;border:2px solid var(--green);color:var(--green-dark);font-weight:700;font-size:20px;display:flex;align-items:center;justify-content:center}
.strengths .result{left:0;top:600px;width:1200px;font-size:42px;font-weight:900}

/* points */
.points{top:2730px;height:660px;background:var(--green-pale)}
.points .top-arrow{left:560px;top:0;width:80px;height:40px;background:var(--white);clip-path:polygon(0 0,100% 0,50% 100%)}
.point-grid{left:60px;top:60px;width:1080px;display:grid;grid-template-columns:1fr 1fr;gap:30px 40px}
.point{background:var(--white);height:260px;position:relative;padding:24px 26px 20px 150px;border:1px solid #d8e4c4}
.point .tag{position:absolute;left:0;top:0;width:80px;height:72px;background:var(--green);color:var(--white);font-weight:900;text-align:center;font-size:13px;padding-top:8px;line-height:1.1}
.point .tag b{display:block;font-size:32px}
.point .thumb{position:absolute;left:22px;top:96px;width:110px;height:130px}
.point h3{font-size:24px;font-weight:900;border-bottom:2px solid var(--green);padding-bottom:8px;margin-bottom:12px}
.point p{font-size:15px;line-height:1.75;color:#444}

/* closing */
.closing{top:3400px;height:296px}
.closing h2{left:0;top:6px;width:1200px;text-align:center;font-size:34px;font-weight:900}
.closing-box{left:60px;top:64px;width:1080px;height:196px;background:linear-gradient(#3b2a1c,#22170f);border:3px solid var(--brown-light)}
.closing-box .mini-cover{left:24px;top:18px;width:140px;height:154px;background:linear-gradient(#5a4634,#2d2219)}
.closing-box .req{left:190px;top:24px;width:560px;height:62px;background:var(--orange);color:var(--white);font-size:30px;font-weight:900;display:flex;align-items:center;justify-content:center;border-radius:6px}
.closing-box .click{left:780px;top:30px;width:260px;height:50px;background:var(--red);color:var(--white);font-size:22px;font-weight:900;border-radius:25px;display:flex;align-items:center;justify-content:center}
.closing-box .tel-note{left:190px;top:110px;width:300px;color:var(--white);font-size:19px;line-height:1.5;font-weight:700}
.closing-box .tel-hours{left:560px;top:100px;color:var(--white);font-size:13px;white-space:nowrap}
.closing-box .tel{left:520px;top:118px;color:var(--white);font-size:52px;font-weight:900;display:flex;align-items:center;gap:14px;letter-spacing:1px;line-height:1.1}
.closing .foot-note{left:60px;top:268px;width:1080px;font-size:11px;line-height:1.5;color:#666;text-align:center}
</style>
</head>
<body>

<header class="site-header">
  <div class="abs brand"><i class="mark"></i><span>玉草工房</span></div>
  <p class="abs tagline">エクステリア専門の施工店 玉草工房。ガーデニングやウッドデッキ、門まわりなど<br>外構工事を幅広く手がけています。地域密着でお庭づくりをお手伝いします。</p>
  <div class="abs contact-btn">
    <span class="icon"><svg width="18" height="14" viewBox="0 0 18 14"><rect x="1" y="1" width="16" height="12" fill="none" stroke="#c8322a" stroke-width="2"/><path d="M1 1l8 7 8-7" fill="none" stroke="#c8322a" stroke-width="2"/></svg></span>
    <span>ガーデンリフォームについての<br>お問い合わせはこちらから</span>
  </div>
</header>

<section class="hero">
  <div class="ph" style="left:0;top:0;width:430px;height:620px;background:radial-gradient(circle at 45% 45%,#f0a0b4,#e3e3de 70%)" role="img" aria-label="ピンクのガーベラの花の写真"></div>
  <div class="ph" style="left:620px;top:420px;width:540px;height:230px;background:linear-gradient(#c9d3c5,#9fa69a)" role="img" aria-label="ガラス張りのガーデンルームの施工写真"></div>
  <div class="abs hero-headline serif">
    <div class="l1">あなたの夢</div>
    <div class="l2">叶えます</div>
  </div>
  <div class="abs hero-copy">
    お客様から、<br>
    「こんなやり方があるなんて全然知らなかった」<br>
    という声をいただきます。<br>
    <span class="em">できるなら理想のエクステリアにしたい。</span><br>
    そんなご要望に玉草工房が全力でお応えします!
  </div>
  <div class="abs free-badge">
    <div class="now">今だけ!</div>
    <div class="free serif">無料<br><span style="font-size:42px">カタログ</span></div>
    <div class="gift">プレゼント中</div>
  </div>
  <div class="abs safe-badge">専門店だから<br>任せて安心!</div>
  <div class="abs service-banner serif">「こだわりのオールインワンサービス」</div>
  <ul class="abs flow">
    <li>ヒアリング</li>
    <li>設計・プランニング</li>
    <li>着工</li>
    <li>お引渡</li>
    <li>アフターケア</li>
  </ul>
</section>

<section class="catalog">
  <div class="abs catalog-cover" role="img" aria-label="施工例カタログの表紙写真">
    <div class="ribbon">施工例たっぷり300ページ!</div>
  </div>
  <h2 class="abs serif">“夢”をカタチに!</h2>
  <p class="abs body">当店のエクステリア工事は、<br>毎月最大5件だけの「ご予約」制です。</p>
  <p class="abs note">先着順でのご予約となりますが、<br>当ホームページをご覧いただいた方のご予約はお断りしておりません。</p>
  <div class="abs cta-btn">
    <svg width="30" height="26" viewBox="0 0 30 26"><rect x="1" y="3" width="13" height="20" fill="none" stroke="#fff" stroke-width="2"/><rect x="16" y="3" width="13" height="20" fill="none" stroke="#fff" stroke-width="2"/></svg>
    カタログ請求はこちら
  </div>
  <div class="abs plan-bubble">まずはカタログで<br>じっくり夢の構想を<br>練って下さい!</div>
</section>

<section class="premium">
  <div class="abs premium-panel">
    <div class="kicker">こだわり×オシャレ</div>
    <div class="big">プレミアム</div>
    <div class="sub">の空間にしてみませんか?</div>
    <p>人それぞれプランニングが異なる時代です。<br>エクステリアの専門家だからこそ、<br>お客様の想いを丁寧にお聞きし、<br>世界にひとつだけの空間をご提案します。</p>
  </div>
  <div class="ph premium-photos" role="img" aria-label="施工中の職人とウッドデッキ、ガーデンライト、門まわりなどの施工例写真" style="background:linear-gradient(135deg,#bcc7a8,#8e8772 55%,#c8bda7)"></div>
</section>

<section class="strengths">
  <h2 class="abs serif">エクステリア専門店だから<br>提案力・施工力に自信があります!</h2>
  <div class="abs pillars">
    <div class="pillar"><span class="label">高度な提案力</span><span class="word">デザイン</span></div>
    <div class="pillar"><span class="label">質の高い工事</span><span class="word">品質</span></div>
    <div class="pillar"><span class="label">適正な価格</span><span class="word">コスト<br>パフォーマンス</span></div>
  </div>
  <div class="abs no-list">
    <div class="no-item">広告費なし</div>
    <div class="no-item">営業マンなし</div>
    <div class="no-item">下請け工事なし</div>
  </div>
  <p class="abs result serif">低コスト経営により実現できました!</p>
</section>

<section class="points">
  <div class="abs top-arrow"></div>
  <div class="abs point-grid">
    <article class="point">
      <div class="tag">POINT<b>1</b></div>
      <div class="ph thumb" style="background:#c7cdb8" role="img" aria-label="施工事例の写真"></div>
      <h3>施工事例の数と質</h3>
      <p>見た目のいいホームページはすぐに作れます。内容の濃い施工事例はすぐには作れません。豊富な施工例こそ専門店の証です。</p>
    </article>
    <article class="point">
      <div class="tag">POINT<b>2</b></div>
      <div class="ph thumb" style="background:#d9cfbd" role="img" aria-label="お客様の写真"></div>
      <h3>お客様からの評判</h3>
      <p>本当に満足できる工事をしてくれるお店なのかを判断する材料として「お客様の声」が重要です。多くの喜びの声をいただいております。</p>
    </article>
    <article class="point">
      <div class="tag">POINT<b>3</b></div>
      <div class="ph thumb" style="background:var(--green-pale);border:2px solid var(--green)"></div>
      <h3>専門店としての誇り</h3>
      <p>「どこよりもお安くします!」という安易な値引きはいたしません。プロとしての誇りに懸けて、ご満足いただける工事をお約束します。</p>
    </article>
    <article class="point">
      <div class="tag">POINT<b>4</b></div>
      <div class="ph thumb" style="background:#cfc6b4" role="img" aria-label="担当スタッフの写真"></div>
      <h3>担当者のレベル</h3>
      <p>コミュニケーションの能力の優れた担当者が対応いたします。説明が難しい言葉も、きちんと具体的に。お客様の想いをカタチにします。</p>
    </article>
  </div>
</section>

<footer class="closing">
  <h2 class="abs serif">玉草工房の豊富な施工例をじっくりご覧下さい。</h2>
  <div class="abs closing-box">
    <div class="abs mini-cover" role="img" aria-label="施工例カタログの表紙写真"></div>
    <div class="abs req">
      <svg width="34" height="28" viewBox="0 0 30 26" style="margin-right:12px"><rect x="1" y="3" width="13" height="20" fill="none" stroke="#fff" stroke-width="2"/><rect x="16" y="3" width="13" height="20" fill="none" stroke="#fff" stroke-width="2"/></svg>
      カタログのご請求はこちらから
    </div>
    <div class="abs click">今すぐクリック ›</div>
    <p class="abs tel-note">お電話でのカタログ請求は<br>右記のフリーダイヤルまで</p>
    <p class="abs tel-hours">カタログ請求専用ダイヤル(受付時間9:00〜18:00)</p>
    <div class="abs tel">
      <svg width="40" height="40" viewBox="0 0 24 24"><path d="M6.6 10.8a15.1 15.1 0 0 0 6.6 6.6l2.2-2.2c.3-.3.7-.4 1-.2 1.1.4 2.3.6 3.6.6.6 0 1 .4 1 1V20c0 .6-.4 1-1 1A17 17 0 0 1 3 4c0-.6.4-1 1-1h3.5c.6 0 1 .4 1 1 0 1.3.2 2.5.6 3.6.1.3 0 .7-.2 1z" fill="#fff"/></svg>
      0120-418-527
    </div>
  </div>
  <p class="abs foot-note">カタログはポルカスなどで販売しているものと同じ内容です。制作費が非常に高いため、在庫が無くなり次第終了となります。<br>ご希望の方はお早めにお申し込み下さい。</p>
</footer>

</body>
</html>
```